Velisa Seafood Shipping Packaging Re-Design

We need a packaging (Shipping Carton) design for our Seafood Products (FROZEN). We already have a basic packaging design which we prefer to have a modern touch on it.
Spec :
1. It must show our logo (Attached), note that the text of "VELISA" which accompany the logo is optional, it can be omitted & showing only the logo.
2. Main color is Blue
3. Our carton is regular shipping box with dimension L43cm x W 27cm x H 16cm.
4. Our material of Carton is both Brown & White Kraft Paperboard, so the design should look nice in both material.

Attached our Logo and packaging design.

Target Market(s)

Frozen Seafood Distributor & Seafood Buyer

Industry/Entity Type

Food Production

Requirements
Must have
• 1. Must Show our Logo
• 2. Main Color of the Text/Logo is Blue
• 3. On the side of the packaging / Carton must show two box of CODE & SIZE
• 4. Must Show these icons :
• a. Handle with Care
• b. Maximum Stackable 10 Carton
• c. Recyleable Material
• d. Protect from the Water/Rain
Nice to have
• Would prefer to have a modern design

```html
<!DOCTYPE html>
<html lang="en">
<head>
<meta charset="utf-8">
<title>Velisa Seafood – Shipping Carton Dieline</title>
<link rel="stylesheet" href="https://fonts.googleapis.com/css2?family=Oswald:wght@500;600&family=Roboto+Condensed:wght@700&display=swap">
<style>
  :root {
    --sky: #3cc0ee;
    --sky-deep: #1e9ad8;
    --ocean: #1f63b3;
    --ocean-light: #2c76c4;
    --navy: #1b2a6e;
    --ice: #eef2f8;
    --frost: #d6e1f0;
    --label: #a9d4f2;
    --badge: #d9ecf8;
    --white: #ffffff;
    --canvas: #ffffff;
  }
  html, body {
    margin: 0;
    padding: 0;
    width: 1200px;
    height: 1200px;
    overflow: hidden;
    background: var(--canvas);
  }
  .carton-dieline {
    position: absolute;
    left: 30px;
    top: 440px;
    width: 1140px;
    height: 241px;
  }
  .panel-text { font-family: "Oswald", sans-serif; font-weight: 600; fill: var(--navy); }
  .box-label { font-family: "Oswald", sans-serif; font-weight: 600; fill: var(--white); }
  .brand-name { font-family: "Oswald", sans-serif; font-weight: 600; fill: var(--ocean); }
  .banner-name { font-family: "Oswald", sans-serif; font-weight: 600; fill: var(--navy); }
  .badge-text { font-family: "Roboto Condensed", sans-serif; font-weight: 700; fill: var(--navy); }
  .icon-ring { fill: none; stroke: var(--white); stroke-width: 1.6; }
  .icon-line { fill: none; stroke: var(--white); stroke-width: 1.4; stroke-linecap: round; stroke-linejoin: round; }
</style>
</head>
<body>
<svg class="carton-dieline" viewBox="0 0 1396 295" xmlns="http://www.w3.org/2000/svg">
  <defs>
    <linearGradient id="flap-sky" x1="0" y1="0" x2="0" y2="1">
      <stop offset="0" stop-color="#3cc0ee"/>
      <stop offset="1" stop-color="#1e9ad8"/>
    </linearGradient>
    <radialGradient id="sky-glow" cx="0.5" cy="0.4" r="0.7">
      <stop offset="0" stop-color="#7fd6f6" stop-opacity="0.55"/>
      <stop offset="1" stop-color="#7fd6f6" stop-opacity="0"/>
    </radialGradient>
    <linearGradient id="band-tone" x1="0" y1="0" x2="1" y2="1">
      <stop offset="0" stop-color="#2468b8"/>
      <stop offset="0.5" stop-color="#1c5aa8"/>
      <stop offset="1" stop-color="#2a70bf"/>
    </linearGradient>
    <radialGradient id="map-tone" cx="0.5" cy="0.5" r="0.75">
      <stop offset="0" stop-color="#f6f8fc"/>
      <stop offset="0.6" stop-color="#e6edf6"/>
      <stop offset="1" stop-color="#cfdcee"/>
    </radialGradient>
    <linearGradient id="grunge-edge" x1="0" y1="0" x2="0" y2="1">
      <stop offset="0" stop-color="#8fb1dd" stop-opacity="0"/>
      <stop offset="0.55" stop-color="#5f8fcf" stop-opacity="0.7"/>
      <stop offset="1" stop-color="#2f6bbf"/>
    </linearGradient>
    <linearGradient id="grunge-side" x1="0" y1="0" x2="1" y2="0">
      <stop offset="0" stop-color="#5f8fcf" stop-opacity="0.55"/>
      <stop offset="1" stop-color="#5f8fcf" stop-opacity="0"/>
    </linearGradient>
    <radialGradient id="emblem-tone" cx="0.5" cy="0.5" r="0.6">
      <stop offset="0" stop-color="#ffffff"/>
      <stop offset="0.6" stop-color="#7fb4e4"/>
      <stop offset="1" stop-color="#1f63b3"/>
    </radialGradient>
    <radialGradient id="seal-fill" cx="0.5" cy="0.45" r="0.6">
      <stop offset="0" stop-color="#ffffff"/>
      <stop offset="1" stop-color="#e4edf8"/>
    </radialGradient>

    <g id="care-icons">
      <circle class="icon-ring" cx="0" cy="0" r="10"/>
      <path class="icon-line" d="M-3.5,-6 H3.5 L2.5,0 Q0,3 -2.5,0 Z M0,2 V6 M-3,6 H3"/>
      <circle class="icon-ring" cx="27" cy="0" r="10"/>
      <path class="icon-line" d="M20,0 Q27,-9 34,0 M27,-1 V5 Q27,7 25,6"/>
      <circle class="icon-ring" cx="54" cy="0" r="10"/>
      <path class="icon-line" d="M48,4 H58 L54,-5 Z"/>
      <circle class="icon-ring" cx="81" cy="0" r="10"/>
      <rect class="icon-line" x="75" y="-6" width="12" height="4"/>
      <rect class="icon-line" x="75" y="-1" width="12" height="4"/>
      <rect class="icon-line" x="75" y="4" width="12" height="3"/>
    </g>
  </defs>

  <!-- ===== front top flap ===== -->
  <g class="flap flap-front">
    <rect x="0" y="0" width="428" height="137" fill="url(#flap-sky)"/>
    <rect x="0" y="0" width="428" height="137" fill="url(#sky-glow)" role="img" aria-label="Soft light bubbles over sky blue"/>
    <ellipse cx="214" cy="4" rx="66" ry="30" fill="url(#emblem-tone)" role="img" aria-label="Engraved fish emblem with sunburst, upside down"/>
    <rect x="328" y="14" width="68" height="26" fill="var(--label)"/>
    <path d="M108,137 Q112,112 140,106 Q150,84 180,80 Q214,74 248,80 Q278,84 288,106 Q316,112 320,137 Z" fill="var(--badge)" stroke="var(--white)" stroke-width="2"/>
    <text class="badge-text" x="268" y="114" font-size="6.5" text-anchor="middle" transform="rotate(180 268 112)">KEEP COOL</text>
    <text class="badge-text" x="166" y="114" font-size="6.5" text-anchor="middle" transform="rotate(180 166 112)">HANDLE WITH CARE</text>
    <text class="brand-name" x="214" y="116" font-size="13" text-anchor="middle" transform="rotate(180 214 111)">VELISA</text>
  </g>

  <!-- ===== back top flap ===== -->
  <g class="flap flap-back">
    <rect x="698" y="0" width="428" height="137" fill="url(#flap-sky)"/>
    <rect x="698" y="0" width="428" height="137" fill="url(#sky-glow)" role="img" aria-label="Soft light bubbles over sky blue"/>
    <rect x="730" y="10" width="68" height="26" fill="var(--label)"/>
    <ellipse cx="912" cy="8" rx="58" ry="28" fill="url(#emblem-tone)" role="img" aria-label="Engraved fish emblem splashing from the waves"/>
    <rect x="844" y="34" width="136" height="18" fill="var(--white)" stroke="var(--navy)" stroke-width="1.4"/>
    <text class="banner-name" x="912" y="48" font-size="14" text-anchor="middle">VELISA SEAFOOD</text>
    <path d="M698,74 C780,58 840,66 912,78 C990,90 1060,84 1126,76 V137 H698 Z" fill="url(#band-tone)" role="img" aria-label="Deep blue wave with faint seafood line pattern"/>
    <path d="M698,74 C780,58 840,66 912,78 C990,90 1060,84 1126,76" fill="none" stroke="var(--navy)" stroke-width="4"/>
  </g>

  <!-- ===== side wall ===== -->
  <rect class="frost-ground" x="0" y="137" width="1396" height="158" fill="url(#map-tone)" role="img" aria-label="Faint vintage world map texture on frosted white ground"/>
  <rect x="0" y="137" width="1396" height="158" fill="url(#map-tone)" opacity="0.5" transform="translate(0 0)"/>

  <g class="panel-folds" role="img" aria-label="Distressed ice-blue edges along the panel folds">
    <rect x="428" y="190" width="14" height="105" fill="url(#grunge-side)"/>
    <rect x="698" y="190" width="14" height="105" fill="url(#grunge-side)"/>
    <rect x="1126" y="190" width="14" height="105" fill="url(#grunge-side)"/>
    <rect x="0" y="190" width="14" height="105" fill="url(#grunge-side)"/>
  </g>

  <g class="seafood-band" role="img" aria-label="Deep blue band with faint line pattern of crabs, lobsters and shells">
    <path d="M0,137 H428 V180 C340,170 240,176 120,188 C70,192 30,192 0,190 Z" fill="url(#band-tone)"/>
    <path d="M428,137 H698 V172 C620,168 540,178 428,190 Z" fill="url(#band-tone)"/>
    <path d="M698,137 H1126 V180 C1040,170 940,176 820,188 C770,192 730,192 698,190 Z" fill="url(#band-tone)"/>
    <path d="M1126,137 H1396 V172 C1318,168 1238,178 1126,190 Z" fill="url(#band-tone)"/>
  </g>

  <rect class="frost-edge" x="0" y="262" width="1396" height="33" fill="url(#grunge-edge)" role="img" aria-label="Rough ice-blue distressed lower edge"/>

  <use href="#care-icons" x="316" y="157"/>
  <use href="#care-icons" x="1014" y="157"/>

  <g class="temp-mark">
    <rect x="56" y="225" width="84" height="30" fill="var(--white)" fill-opacity="0.6" stroke="var(--navy)" stroke-width="1.6"/>
    <rect x="62" y="231" width="5" height="16" rx="2.5" fill="none" stroke="var(--navy)" stroke-width="1.2"/>
    <circle cx="64.5" cy="248" r="3" fill="var(--navy)"/>
    <text class="panel-text" x="104" y="249" font-size="22" text-anchor="middle">-18°C</text>
  </g>
  <g class="temp-mark">
    <rect x="754" y="225" width="84" height="30" fill="var(--white)" fill-opacity="0.6" stroke="var(--navy)" stroke-width="1.6"/>
    <rect x="760" y="231" width="5" height="16" rx="2.5" fill="none" stroke="var(--navy)" stroke-width="1.2"/>
    <circle cx="762.5" cy="248" r="3" fill="var(--navy)"/>
    <text class="panel-text" x="802" y="249" font-size="22" text-anchor="middle">-18°C</text>
  </g>

  <g class="spec-boxes">
    <rect x="462" y="204" width="98" height="30" fill="none" stroke="var(--navy)" stroke-width="1.4"/>
    <rect x="462" y="204" width="34" height="30" fill="var(--navy)"/>
    <text class="box-label" x="479" y="225" font-size="14" text-anchor="middle">SIZE</text>
    <rect x="462" y="244" width="98" height="30" fill="none" stroke="var(--navy)" stroke-width="1.4"/>
    <rect x="462" y="244" width="34" height="30" fill="var(--navy)"/>
    <text class="box-label" x="479" y="265" font-size="13" text-anchor="middle">CODE</text>
  </g>
  <g class="spec-boxes">
    <rect x="1160" y="204" width="98" height="30" fill="none" stroke="var(--navy)" stroke-width="1.4"/>
    <rect x="1160" y="204" width="34" height="30" fill="var(--navy)"/>
    <text class="box-label" x="1177" y="225" font-size="14" text-anchor="middle">SIZE</text>
    <rect x="1160" y="244" width="98" height="30" fill="none" stroke="var(--navy)" stroke-width="1.4"/>
    <rect x="1160" y="244" width="34" height="30" fill="var(--navy)"/>
    <text class="box-label" x="1177" y="265" font-size="13" text-anchor="middle">CODE</text>
  </g>

  <g class="brand-seal">
    <circle cx="217" cy="239" r="47" fill="url(#seal-fill)" stroke="var(--navy)" stroke-width="1.6"/>
    <text class="brand-name" x="217" y="246" font-size="20" text-anchor="middle">VELISA</text>
  </g>
  <g class="brand-seal">
    <circle cx="645" cy="239" r="47" fill="url(#seal-fill)" stroke="var(--navy)" stroke-width="1.6"/>
    <text class="brand-name" x="645" y="246" font-size="20" text-anchor="middle">VELISA</text>
  </g>
  <g class="brand-seal">
    <circle cx="915" cy="239" r="47" fill="url(#seal-fill)" stroke="var(--navy)" stroke-width="1.6"/>
    <text class="brand-name" x="915" y="246" font-size="20" text-anchor="middle">VELISA</text>
  </g>
  <g class="brand-seal">
    <circle cx="1343" cy="239" r="47" fill="url(#seal-fill)" stroke="var(--navy)" stroke-width="1.6"/>
    <text class="brand-name" x="1343" y="246" font-size="20" text-anchor="middle">VELISA</text>
  </g>
</svg>
</body>
</html>
```